TideLantern business card design

I would like a design that shows people that TideLantern is about using SOUND as a tool in ALL areas and stages of life - during labour, during motherhood, when a baby, child, adult at work, while sick, when dying, when celebrating.... there are MANY different pathways that the power of sound can be incorporated to help people relax, energise and connect with themselves and others.
The logo is purple...I can see pathways, swirling, colours, musical notes or sound waves.... white background on front. Can have different colour on back...I'm flexible and open to suggestions.

Target Market(s)

at the moment it is mostly expectant couples and mothers... but it really is for anyone who is looking for an alternative to "traditional" medicine

Industry/Entity Type

Adult

Contact Information for Business Card

Marisa Quentin - founder
0473916284
www.tidelantern.com.au
marisa@tidelantern.com.au
tidecradle
tidegames
tidenourish
tiderituals
tidekneading

Colors

Designer to choose colors to be used in the design.

Requirements
Must have
• logo
music notes/soundwaves - something that represents sound affecting people
something that represents pathways and/or connection

```html
<!DOCTYPE html>
<html lang="en">
<head>
<meta charset="utf-8">
<title>TideLantern business card</title>
<link rel="stylesheet" href="https://fonts.googleapis.com/css2?family=Questrial&family=Montserrat:wght@700&display=swap">
<style>
  :root {
    --backdrop: #b9b9bb;
    --plum: #8c1d86;
    --plum-deep: #5a0e57;
    --plum-light: #a8399f;
    --ink: #2a2a2a;
    --ink-soft: #555555;
    --mark-grey: #e3e3e3;
    --paper: #ffffff;
  }
  * { margin: 0; padding: 0; box-sizing: border-box; }
  html, body { width: 1200px; height: 871px; overflow: hidden; }
  body {
    background: var(--backdrop);
    font-family: "Questrial", "Century Gothic", sans-serif;
    position: relative;
  }
  .card {
    position: absolute;
    width: 540px;
    height: 308px;
    box-shadow: 0 10px 24px rgba(0,0,0,0.25);
    overflow: hidden;
  }

  /* Back side */
  .card-back {
    left: 50px; top: 130px;
    background: linear-gradient(135deg, var(--plum-light) 0%, var(--plum) 45%, var(--plum-deep) 100%);
    color: var(--paper);
  }
  .card-back .brand {
    position: absolute;
    left: 0; right: 0; top: 92px;
    text-align: center;
  }
  .card-back .brand-name {
    font-size: 48px;
    letter-spacing: 0.5px;
    line-height: 1;
  }
  .card-back .tagline {
    margin-top: 12px;
    font-size: 17px;
    opacity: 0.85;
  }
  .card-back .tagline strong { font-weight: normal; opacity: 1; }
  .services {
    position: absolute;
    left: 0; right: 0; bottom: 26px;
    text-align: center;
    font-size: 13px;
    letter-spacing: 0.3px;
    opacity: 0.9;
  }
  .services .sep { margin: 0 6px; }

  /* Front side */
  .card-front {
    left: 610px; top: 430px;
    background: var(--paper);
    color: var(--ink);
  }
  .card-front .brand {
    position: absolute;
    left: 34px; top: 86px;
  }
  .brand-row { display: flex; align-items: center; gap: 12px; }
  .brand-dot {
    width: 46px; height: 46px;
    border-radius: 50%;
    background: var(--mark-grey);
  }
  .card-front .brand-name {
    font-size: 40px;
    color: var(--plum);
    line-height: 1;
  }
  .card-front .tagline {
    margin-top: 14px;
    font-size: 16px;
    color: var(--ink);
  }
  .card-front .tagline strong { font-weight: normal; color: #000; }

  .contact {
    position: absolute;
    left: 318px; top: 92px;
  }
  .contact .person {
    font-family: "Montserrat", "Arial", sans-serif;
    font-weight: 700;
    font-size: 15px;
    color: var(--ink);
    margin-left: 22px;
  }
  .contact .role {
    font-size: 12px;
    color: var(--plum);
    margin: 4px 0 30px 22px;
  }
  .contact ul { list-style: none; }
  .contact li {
    display: flex; align-items: center; gap: 10px;
    font-size: 12px;
    color: var(--ink-soft);
    margin-bottom: 13px;
  }
  .contact svg { width: 13px; height: 13px; flex: none; }
</style>
</head>
<body>

  <section class="card card-back" aria-label="Card back">
    <div class="brand">
      <div class="brand-name">TideLantern</div>
      <p class="tagline">every stage gently <strong>held</strong></p>
    </div>
    <p class="services">
      tidecradle<span class="sep">|</span>tidegames<span class="sep">|</span>tidenourish<span class="sep">|</span>tiderituals<span class="sep">|</span>tidekneading
    </p>
  </section>

  <section class="card card-front" aria-label="Card front">
    <div class="brand">
      <div class="brand-row">
        <span class="brand-dot"></span>
        <span class="brand-name">TideLantern</span>
      </div>
      <p class="tagline">every stage gently <strong>held</strong></p>
    </div>

    <div class="contact">
      <p class="person">Marisa Quentin</p>
      <p class="role">founder</p>
      <ul>
        <li>
          <svg viewBox="0 0 16 16" aria-hidden="true"><path fill="var(--plum)" d="M4 1.5l2.3 2.6-1.2 1.6c.8 1.9 2.3 3.4 4.2 4.2l1.6-1.2 2.6 2.3-1.3 2.1C6.8 12.9 3.1 9.2 1.9 3.8z"/></svg>
          <span>0473916284</span>
        </li>
        <li>
          <svg viewBox="0 0 16 16" aria-hidden="true"><rect x="1" y="3" width="14" height="10" fill="none" stroke="var(--plum)" stroke-width="1.5"/><path d="M1 3.5l7 5 7-5" fill="none" stroke="var(--plum)" stroke-width="1.5"/></svg>
          <span>marisa@tidelantern.com.au</span>
        </li>
        <li>
          <svg viewBox="0 0 16 16" aria-hidden="true"><circle cx="8" cy="8" r="6.5" fill="none" stroke="var(--plum)" stroke-width="1.5"/><ellipse cx="8" cy="8" rx="2.8" ry="6.5" fill="none" stroke="var(--plum)" stroke-width="1.2"/><path d="M1.5 8h13" stroke="var(--plum)" stroke-width="1.2"/></svg>
          <span>www.tidelantern.com.au</span>
        </li>
      </ul>
    </div>
  </section>

</body>
</html>
```